need professional, precise design for a website

I will start with a homepage design and if we pick your design, we'll have you design up to 6 more interior pages (we'll pay extra for these of course). We need a homepage design for a reserve study company based in Idaho, covering the northwest region. The company is called copper ridge reserve study. Their current site is at https://www.copperridgereserves.example/ and they really like this site for inspiration https://www.fundplannerhub.example/ but they would like an original design, just more modern and fresh like the sample site. I have logo files I will attach. They want something that looks financial and has a feel of accuity. Their main call to action will be to have someone fill in a contact form or call them on the phone. They will have a sample study that someone can download as on the fundplannerhub site. You can use copy from their current site.

```html
<!DOCTYPE html>
<html lang="en">
<head>
<meta charset="utf-8">
<title>Copper Ridge Reserves — Reserve Studies</title>
<link rel="stylesheet" href="https://fonts.googleapis.com/css2?family=Roboto:wght@300;400;500;700&display=swap">
<style>
  :root{
    --navy:#11427c;
    --navy-deep:#1f2a5c;
    --stat-blue:#3b78c0;
    --sky-a:#2f5fb0;
    --sky-b:#9cbbe3;
    --cyan:#0aa9e8;
    --cyan-text:#12a3e0;
    --pale:#eef7fb;
    --green:#1fb45a;
    --grey-text:#55585f;
    --nav-grey:#6b6f78;
    --footer:#cdd1d8;
    --white:#ffffff;
  }
  *{box-sizing:border-box;margin:0;padding:0}
  html,body{width:712px;height:1200px;overflow:hidden;background:var(--white)}
  body{font-family:"Roboto",Arial,sans-serif;color:var(--grey-text);position:relative}
  .abs{position:absolute}

  /* header */
  .site-header{left:0;top:0;width:712px;height:54px;background:var(--white)}
  .brand{display:flex;align-items:center;gap:5px;font-size:13px;font-weight:400;color:var(--navy-deep);letter-spacing:.3px;white-space:nowrap}
  .brand-dot{width:9px;height:9px;border-radius:50%;background:var(--navy-deep)}
  .site-header .brand{left:86px;top:20px}
  .main-nav{top:31px;font-size:8.5px;color:var(--nav-grey);letter-spacing:.2px}
  .main-nav span{position:absolute;white-space:nowrap}

  /* hero */
  .hero{left:0;top:54px;width:712px;height:269px;background:linear-gradient(160deg,var(--sky-a) 0%,#5d86c8 45%,var(--sky-b) 100%)}
  .hero-photo{left:120px;top:40px;width:220px;height:229px;background:linear-gradient(180deg,#e9e6dc 0%,#d4d0c4 55%,#2a2a2e 100%);opacity:.85}
  .hero-title{left:360px;top:68px;font-size:28.5px;line-height:34px;font-weight:400;color:var(--navy-deep);letter-spacing:.3px}
  .hero-call{left:354px;top:216px;font-size:17px;font-weight:500;color:var(--white)}
  .btn-quick{left:531px;top:210px;width:150px;height:28px;background:var(--cyan);border-radius:4px;color:var(--white);font-size:12.5px;display:flex;align-items:center;justify-content:center;box-shadow:0 2px 4px rgba(0,0,0,.25)}

  /* stats */
  .stat{color:var(--stat-blue)}
  .stat-num{font-size:54px;font-weight:700;line-height:1}
  .stat-label{font-size:12.5px;font-weight:500;line-height:14px;margin-top:6px}
  .stat-rule{width:1px;height:76px;background:var(--stat-blue);top:361px}

  /* services */
  .services{left:0;top:457px;width:712px;height:233px;background:var(--pale)}
  .service-icon{width:48px;height:48px;border:1.2px solid var(--cyan-text);border-radius:50%;background:var(--white)}
  .service-title{font-size:8px;line-height:10px;color:var(--cyan-text);text-transform:uppercase}
  .service-text{font-size:6.8px;line-height:8.5px;width:124px;color:var(--grey-text)}
  .btn-more{width:61px;height:16px;border-radius:4px;background:var(--navy);color:var(--white);font-size:7px;font-weight:500;display:flex;align-items:center;justify-content:center}

  /* callback */
  .callback{left:0;top:690px;width:712px;height:148px;background:var(--navy)}
  .callback h2{position:absolute;left:84px;top:49px;font-size:12px;font-weight:700;color:var(--white)}
  .callback p{position:absolute;left:84px;top:68px;width:130px;font-size:5.6px;line-height:7px;font-weight:500;color:#d7e2f0}
  .field{width:145px;height:21px;background:var(--cyan);color:var(--white);font-size:6.5px;font-weight:500;padding-left:11px;display:flex;align-items:center}
  .btn-submit{left:578px;top:63px;width:47px;height:18px;background:var(--green);color:var(--white);font-size:5px;font-weight:700;display:flex;align-items:center;justify-content:center}

  .skyline{left:175px;top:850px;width:380px;height:195px;background:linear-gradient(180deg,#f1f7fb 0%,#f8ebe3 55%,#eef4ee 100%)}

  /* footer */
  .site-footer{left:0;top:1045px;width:712px;height:155px;background:var(--footer)}
  .site-footer .brand{left:94px;top:25px;font-size:11px}
  .footer-nav{top:32px;font-size:7px;color:var(--nav-grey)}
  .footer-nav span{position:absolute;white-space:nowrap}
  .footer-info{left:98px;top:54px;font-size:6.6px;line-height:11.5px;color:#444}
  .social{top:63px;width:11px;height:11px;border-radius:50%;background:#6a6d73}
  .copyright{left:0;top:126px;width:712px;text-align:center;font-size:6.5px;color:#333}
</style>
</head>
<body>

<header class="site-header abs">
  <div class="brand abs"><span class="brand-dot"></span>Copper Ridge Reserves</div>
  <nav class="main-nav abs">
    <span style="left:366px">WHO WE ARE</span>
    <span style="left:452px">RESERVE STUDIES ▾</span>
    <span style="left:558px">CONTACT</span>
  </nav>
</header>

<section class="hero abs">
  <div class="hero-photo abs" role="img" aria-label="Photo of a businessman holding an unfolded road map against a cloudy blue sky"></div>
  <h1 class="hero-title abs">YOUR FINANCIAL<br>ROAD MAP FOR<br>THE NEXT 30 YEARS!</h1>
  <div class="hero-call abs">CALL (208) 555-0142</div>
  <div class="btn-quick abs">QUCK CONTACT</div>
</section>

<section class="stats">
  <div class="stat abs" style="left:158px;top:354px"><div class="stat-num">50</div><div class="stat-label" style="margin-left:6px">CITIES<br>SERVED</div></div>
  <div class="stat-rule abs" style="left:265px"></div>
  <div class="stat abs" style="left:296px;top:354px"><div class="stat-num">100+</div><div class="stat-label" style="margin-left:8px">PROJECT<br>ENGAGEMENTS</div></div>
  <div class="stat-rule abs" style="left:453px"></div>
  <div class="stat abs" style="left:477px;top:354px"><div class="stat-num">20+</div><div class="stat-label" style="margin-left:3px;margin-top:14px">EXPERIENCE</div></div>
</section>

<section class="services abs">
  <div class="service-icon abs" style="left:142px;top:13px">
    <svg width="48" height="48" viewBox="0 0 48 48" fill="none" stroke="#12a3e0" stroke-width="1.6"><rect x="14" y="17" width="20" height="18"/><rect x="18" y="21" width="4" height="4"/><rect x="26" y="21" width="4" height="4"/><rect x="18" y="28" width="4" height="4"/><rect x="26" y="28" width="4" height="4"/><path d="M20 17v-4h8v4"/></svg>
  </div>
  <div class="service-icon abs" style="left:303px;top:13px">
    <svg width="48" height="48" viewBox="0 0 48 48"><rect x="18" y="11" width="12" height="25" fill="#12a3e0"/><g fill="#fff"><rect x="20" y="14" width="2" height="2"/><rect x="26" y="14" width="2" height="2"/><rect x="20" y="19" width="2" height="2"/><rect x="26" y="19" width="2" height="2"/><rect x="20" y="24" width="2" height="2"/><rect x="26" y="24" width="2" height="2"/><rect x="22" y="30" width="4" height="6"/></g></svg>
  </div>
  <div class="service-icon abs" style="left:476px;top:13px">
    <svg width="48" height="48" viewBox="0 0 48 48" fill="none" stroke="#12a3e0" stroke-width="1.6"><path d="M13 34h22M15 34V22h18v12M17 26h14M17 29h14M19 22v-6M29 22v-6"/></svg>
  </div>

  <div class="service-title abs" style="left:144px;top:75px">HOA &amp;<br>CONDOMINIUM STUDIES</div>
  <div class="service-title abs" style="left:305px;top:75px">COMMERCIAL, VACATION &amp;<br>TIME SHARE</div>
  <div class="service-title abs" style="left:479px;top:75px">PARKS &amp;<br>PUBLIC LANDS</div>

  <p class="service-text abs" style="left:144px;top:104px">Every homeowners association is different. Different sets of assets, different financials and different historical backgrounds that have brought you to the present. Each of these is taken into consideration to customize your 30 year budget and build the most accurate, most precise long-term savings ("reserve") report you can buy.</p>
  <p class="service-text abs" style="left:305px;top:104px">Your property represents a significant capital investment. In many cases, your business is dependent on the livelihood and functionality of the edifice in which it resides. We believe a fiscally sound plan and budget of capital expenses is as essential as the building itself. We are comprehensive, thorough and intense about our calculations.</p>
  <p class="service-text abs" style="left:479px;top:104px">Much like HOA's and condominiums, you have finite funds that originate from a constituent base of tax payers. Planning the use of these funds and repairs and/or maintenance of public assets is essential to transparency and candid communication with your constituents. Being in control of the future starts with a financial plan.</p>

  <div class="btn-more abs" style="left:145px;top:198px">MORE</div>
  <div class="btn-more abs" style="left:306px;top:198px">MORE</div>
  <div class="btn-more abs" style="left:479px;top:198px">MORE</div>
</section>

<section class="callback abs">
  <h2>REQUEST CALL BACK.</h2>
  <p>Would you like to speak to one of our financial advisers over the phone? Just submit your details and we'll be in touch shortly. You can also email us if you would prefer.</p>
  <div class="field abs" style="left:240px;top:47px;justify-content:space-between;padding-right:8px">how can we help? <span>▾</span></div>
  <div class="field abs" style="left:400px;top:47px;padding-left:17px">you phone number*</div>
  <div class="field abs" style="left:240px;top:83px">You name*</div>
  <div class="field abs" style="left:400px;top:83px;padding-left:17px">you email</div>
  <div class="btn-submit abs">SUBMIT &nbsp;›</div>
</section>

<div class="skyline abs" role="img" aria-label="Faint pastel illustration of a city skyline"></div>

<footer class="site-footer abs">
  <div class="brand abs"><span class="brand-dot"></span>Copper Ridge Reserves</div>
  <nav class="footer-nav abs">
    <span style="left:405px">WHO WE ARE</span>
    <span style="left:490px">SERVICES</span>
    <span style="left:555px">SERVICES</span>
    <span style="left:619px">CONTACT</span>
  </nav>
  <div class="footer-info abs">
    Copper Ridge Reserves, LLC<br>
    Serving Idaho, Montana, Oregon, Utah, Washington &amp; Wyoming<br>
    Phone: &nbsp;&nbsp;&nbsp;(208) 555-0142<br>
    E-mail: &nbsp;&nbsp;Dana@CopperRidgeReserves.example
  </div>
  <span class="social abs" style="left:500px"></span>
  <span class="social abs" style="left:523px"></span>
  <span class="social abs" style="left:545px"></span>
  <span class="social abs" style="left:567px"></span>
  <div class="copyright abs">Copyright © COPPER RIDGE RESERVES 2019. All Rights Reserved</div>
</footer>

</body>
</html>
```